IT-Dienstleister für Projektmanagementsoftware sucht Broschüre im DIN-A4-Format
Zielgruppe
Wir sind ein IT-Dienstleister für Projektmanagementsoftware. Wir installieren, migrieren und entwickeln Software für das Projektmanagement auf Basis von Veltrano Technologien. Unsere Zielgruppe sind mittelständische Unternehmen und große Konzerne. Je komplexer das Projektmanagement in einem Unternehmen, desto eher helfen unsere Lösungen.
Aufgabenstellung
Es soll eine DIN A4 Hochglanz Broschüre für eine Messe entstehen. Wir haben bereits ein Grobkonzept mit Bildauswahl und Texten erstellt. An diesem soll sich orientiert werden. Bezüglich desDesigns, der Anordnung der Texte und Bilder etc. besteht völlige Freiheit. Weitere Orientierung bieten unsere Webseiten haldewiegand.de und quilbyte.de. Die Texte und Screenshots sind teilweise nur Platzhalter und müssen später noch angepasst werden können. Wir benötigen daher unbedingt die Rohdaten des Designs.

```html
<!DOCTYPE html>
<html lang="de">
<head>
<meta charset="utf-8">
<title>Halde &amp; Wiegand – Broschüre</title>
<link rel="stylesheet" href="https://fonts.googleapis.com/css2?family=Montserrat:wght@300;400&family=Open+Sans:wght@300;400;600;700&display=swap">
<style>
:root{
  --green:#8fbc3b;
  --green-dark:#76a22c;
  --ink:#4a4a4a;
  --muted:#8a8a8a;
  --paper:#ffffff;
  --stage:#dcdcdc;
  --ui-bg:#f7f8f5;
}
*{box-sizing:border-box;margin:0;padding:0}
html,body{width:1200px;height:2400px;overflow:hidden}
body{background:var(--stage);font-family:"Open Sans",Arial,sans-serif;color:var(--ink);position:relative}
.sheet{position:absolute;background:var(--paper);box-shadow:0 6px 14px rgba(0,0,0,.18);overflow:hidden}
.cover{width:270px;height:382px}
.spread{width:540px;height:382px}
.spread::after{content:"";position:absolute;left:255px;top:0;width:30px;height:100%;background:linear-gradient(90deg,rgba(0,0,0,0),rgba(0,0,0,.12) 50%,rgba(0,0,0,0));pointer-events:none}
.el,.photo,.screenshot{position:absolute}
.screenshot{border:1.5px solid var(--green);background:#fff;padding:3px;display:block}
.screenshot svg{display:block;width:100%;height:100%}
.green-page{position:absolute;top:0;height:100%;background:var(--green)}
.running-head{position:absolute;top:20px;font-size:4px;font-weight:700;letter-spacing:.6px;color:var(--green);text-transform:uppercase}
.body-copy{position:absolute;font-size:4.3px;line-height:1.65;color:var(--ink)}
.body-copy p+p{margin-top:4px}
.caption{position:absolute;font-size:4.1px;line-height:1.6;color:var(--green)}
.product-title{position:absolute;font-weight:700;font-size:17px;letter-spacing:.4px;color:#fff;text-transform:uppercase;text-shadow:0 1px 2px rgba(0,0,0,.35);white-space:nowrap}
.tagline{position:absolute;display:flex;flex-direction:column;align-items:flex-start;gap:2px}
.tagline span{background:var(--green);color:#fff;font-weight:300;font-size:10px;line-height:1.3;padding:0 4px;white-space:nowrap}
.page-foot{position:absolute;bottom:16px;height:1px;background:var(--green);opacity:.6}
.page-foot-text{position:absolute;bottom:8px;font-size:3.4px;letter-spacing:.5px;color:var(--muted)}
.brand{position:absolute;font-family:"Montserrat","Open Sans",sans-serif;font-weight:300;color:#444;white-space:nowrap}
.brand .name{display:block;font-size:14px;letter-spacing:.2px}
.brand .sub{display:block;font-size:7.4px;letter-spacing:.4px;margin-top:-1px}
.brand .rule{display:block;height:2px;background:var(--green);margin-top:3px}
.brand.light{color:#fff}
.brand.light .rule{background:#fff}
.headline-bars{position:absolute;display:flex;flex-direction:column;align-items:flex-start;gap:4px}
.headline-bars span{background:#fff;color:#333;font-family:"Montserrat","Open Sans",sans-serif;font-weight:300;font-size:21px;line-height:1.3;padding:0 8px;white-space:nowrap}
.quote-box{position:absolute;background:var(--green);color:#fff;padding:9px 10px}
.quote-box .quote{font-weight:600;font-size:5.6px;line-height:1.5;letter-spacing:.2px}
.quote-box .author{font-size:4px;line-height:1.6;margin-top:10px}
.partner-box{position:absolute;background:#fff;padding:12px}
.partner-row{display:flex;gap:12px;margin-top:14px}
.partner-name{display:flex;align-items:center;gap:3px;font-size:5.6px;white-space:nowrap}
.partner-name i{display:block;width:6px;height:6px}
.partner-word{font-size:10px;color:#555}
.badge{display:flex;align-items:center;gap:6px;margin-top:16px}
.badge-shape{width:28px;height:18px;background:#777}
.badge-lines{font-size:3.4px;line-height:1.6;color:var(--muted)}
.section-heading{position:absolute;font-size:5.5px;font-weight:600;color:var(--green)}
</style>
</head>
<body>

<svg width="0" height="0" style="position:absolute" aria-hidden="true">
  <defs>
    <symbol id="ui-list" viewBox="0 0 200 100" preserveAspectRatio="none">
      <rect width="200" height="100" fill="#fff"/>
      <rect width="200" height="6" fill="#3a6fb0"/>
      <rect x="4" y="10" width="44" height="3" fill="#8fbc3b"/>
      <g fill="#cfcfcf"><rect x="4" y="20" width="26" height="2"/><rect x="4" y="26" width="22" height="2"/><rect x="4" y="32" width="28" height="2"/><rect x="4" y="38" width="20" height="2"/><rect x="4" y="44" width="24" height="2"/></g>
      <rect x="40" y="18" width="156" height="5" fill="#e6e6e6"/>
      <g stroke="#ededed" stroke-width=".6"><line x1="40" y1="30" x2="196" y2="30"/><line x1="40" y1="38" x2="196" y2="38"/><line x1="40" y1="46" x2="196" y2="46"/><line x1="40" y1="54" x2="196" y2="54"/><line x1="40" y1="62" x2="196" y2="62"/><line x1="40" y1="70" x2="196" y2="70"/><line x1="40" y1="78" x2="196" y2="78"/><line x1="40" y1="86" x2="196" y2="86"/></g>
      <g fill="#5b8fd0"><rect x="42" y="26" width="30" height="2"/><rect x="42" y="34" width="26" height="2"/><rect x="42" y="42" width="34" height="2"/><rect x="42" y="50" width="22" height="2"/><rect x="42" y="58" width="30" height="2"/><rect x="42" y="66" width="28" height="2"/><rect x="42" y="74" width="24" height="2"/><rect x="42" y="82" width="32" height="2"/></g>
      <g fill="#bdbdbd"><rect x="90" y="26" width="20" height="2"/><rect x="90" y="34" width="20" height="2"/><rect x="90" y="42" width="20" height="2"/><rect x="90" y="50" width="20" height="2"/><rect x="90" y="58" width="20" height="2"/><rect x="90" y="66" width="20" height="2"/><rect x="90" y="74" width="20" height="2"/><rect x="90" y="82" width="20" height="2"/>
      <rect x="125" y="26" width="16" height="2"/><rect x="125" y="34" width="16" height="2"/><rect x="125" y="42" width="16" height="2"/><rect x="125" y="50" width="16" height="2"/><rect x="125" y="58" width="16" height="2"/><rect x="125" y="66" width="16" height="2"/></g>
      <g fill="#8fbc3b"><rect x="155" y="25" width="30" height="3"/><rect x="155" y="41" width="18" height="3"/><rect x="155" y="57" width="24" height="3"/></g>
      <g fill="#d9534f"><rect x="155" y="33" width="12" height="3"/><rect x="155" y="65" width="20" height="3"/></g>
      <rect x="155" y="49" width="26" height="3" fill="#e8b300"/>
    </symbol>

    <symbol id="ui-heat" viewBox="0 0 200 120" preserveAspectRatio="none">
      <rect width="200" height="120" fill="#fff"/>
      <rect width="200" height="6" fill="#3a6fb0"/>
      <rect x="4" y="10" width="30" height="3" fill="#666"/>
      <g fill="#cfcfcf"><rect x="4" y="20" width="24" height="2"/><rect x="4" y="26" width="20" height="2"/><rect x="4" y="32" width="26" height="2"/><rect x="4" y="38" width="18" height="2"/></g>
      <g>
        <rect x="70" y="12" width="9" height="7" fill="#e8b300"/><rect x="79" y="12" width="9" height="7" fill="#e07b2a"/><rect x="88" y="12" width="9" height="7" fill="#d9534f"/><rect x="97" y="12" width="9" height="7" fill="#d9534f"/>
        <rect x="70" y="19" width="9" height="7" fill="#8fbc3b"/><rect x="79" y="19" width="9" height="7" fill="#e8b300"/><rect x="88" y="19" width="9" height="7" fill="#e07b2a"/><rect x="97" y="19" width="9" height="7" fill="#d9534f"/>
        <rect x="70" y="26" width="9" height="7" fill="#8fbc3b"/><rect x="79" y="26" width="9" height="7" fill="#8fbc3b"/><rect x="88" y="26" width="9" height="7" fill="#e8b300"/><rect x="97" y="26" width="9" height="7" fill="#e07b2a"/>
        <rect x="70" y="33" width="9" height="7" fill="#5aa02c"/><rect x="79" y="33" width="9" height="7" fill="#8fbc3b"/><rect x="88" y="33" width="9" height="7" fill="#8fbc3b"/><rect x="97" y="33" width="9" height="7" fill="#e8b300"/>
      </g>
      <rect x="4" y="46" width="192" height="5" fill="#e6e6e6"/>
      <g fill="#5b8fd0"><rect x="6" y="55" width="50" height="2"/><rect x="6" y="61" width="44" height="2"/><rect x="6" y="67" width="52" height="2"/><rect x="6" y="73" width="40" height="2"/><rect x="6" y="79" width="48" height="2"/><rect x="6" y="85" width="46" height="2"/><rect x="6" y="91" width="50" height="2"/><rect x="6" y="97" width="38" height="2"/><rect x="6" y="103" width="44" height="2"/><rect x="6" y="109" width="50" height="2"/></g>
      <g fill="#bdbdbd"><rect x="70" y="55" width="26" height="2"/><rect x="70" y="61" width="26" height="2"/><rect x="70" y="67" width="26" height="2"/><rect x="70" y="73" width="26" height="2"/><rect x="70" y="79" width="26" height="2"/><rect x="70" y="85" width="26" height="2"/><rect x="70" y="91" width="26" height="2"/><rect x="70" y="97" width="26" height="2"/><rect x="70" y="103" width="26" height="2"/><rect x="70" y="109" width="26" height="2"/></g>
      <g fill="#8fbc3b"><rect x="104" y="54" width="10" height="4"/><rect x="104" y="66" width="10" height="4"/><rect x="104" y="78" width="10" height="4"/><rect x="104" y="90" width="10" height="4"/><rect x="104" y="102" width="10" height="4"/></g>
      <g fill="#d9534f"><rect x="104" y="60" width="10" height="4"/><rect x="104" y="84" width="10" height="4"/></g>
      <g fill="#e8b300"><rect x="104" y="72" width="10" height="4"/><rect x="104" y="96" width="10" height="4"/><rect x="104" y="108" width="10" height="4"/></g>
      <g fill="#cfcfcf"><rect x="124" y="55" width="70" height="2"/><rect x="124" y="61" width="64" height="2"/><rect x="124" y="67" width="70" height="2"/><rect x="124" y="73" width="60" height="2"/><rect x="124" y="79" width="70" height="2"/><rect x="124" y="85" width="66" height="2"/><rect x="124" y="91" width="70" height="2"/><rect x="124" y="97" width="58" height="2"/><rect x="124" y="103" width="70" height="2"/><rect x="124" y="109" width="64" height="2"/></g>
    </symbol>

    <symbol id="ui-gantt" viewBox="0 0 200 110" preserveAspectRatio="none">
      <rect width="200" height="110" fill="#fff"/>
      <rect width="200" height="6" fill="#2f7a3a"/>
      <g fill="#e6e6e6"><rect x="0" y="6" width="200" height="8"/></g>
      <g fill="#9a9a9a"><rect x="6" y="9" width="14" height="2"/><rect x="26" y="9" width="14" height="2"/><rect x="46" y="9" width="14" height="2"/><rect x="66" y="9" width="14" height="2"/></g>
      <rect x="0" y="14" width="12" height="96" fill="#eef3e6"/>
      <g stroke="#ececec" stroke-width=".6"><line x1="12" y1="24" x2="200" y2="24"/><line x1="12" y1="32" x2="200" y2="32"/><line x1="12" y1="40" x2="200" y2="40"/><line x1="12" y1="48" x2="200" y2="48"/><line x1="12" y1="56" x2="200" y2="56"/><line x1="12" y1="64" x2="200" y2="64"/><line x1="12" y1="72" x2="200" y2="72"/><line x1="12" y1="80" x2="200" y2="80"/><line x1="12" y1="88" x2="200" y2="88"/><line x1="12" y1="96" x2="200" y2="96"/>
      <line x1="70" y1="16" x2="70" y2="106"/><line x1="100" y1="16" x2="100" y2="106"/><line x1="130" y1="16" x2="130" y2="106"/><line x1="160" y1="16" x2="160" y2="106"/></g>
      <g fill="#bdbdbd"><rect x="16" y="20" width="40" height="2"/><rect x="16" y="28" width="34" height="2"/><rect x="16" y="36" width="44" height="2"/><rect x="16" y="44" width="30" height="2"/><rect x="16" y="52" width="38" height="2"/><rect x="16" y="60" width="42" height="2"/><rect x="16" y="68" width="32" height="2"/><rect x="16" y="76" width="40" height="2"/><rect x="16" y="84" width="36" height="2"/><rect x="16" y="92" width="44" height="2"/></g>
      <g fill="#c7c7c7"><rect x="74" y="20" width="16" height="2"/><rect x="104" y="20" width="16" height="2"/><rect x="134" y="20" width="16" height="2"/><rect x="74" y="36" width="16" height="2"/><rect x="134" y="44" width="16" height="2"/><rect x="104" y="60" width="16" height="2"/><rect x="164" y="68" width="16" height="2"/><rect x="74" y="84" width="16" height="2"/></g>
      <rect x="58" y="34" width="84" height="56" fill="#fff" stroke="#9a9a9a" stroke-width=".8"/>
      <rect x="58" y="34" width="84" height="6" fill="#f0d48a"/>
      <g fill="#cfcfcf"><rect x="62" y="44" width="30" height="2"/><rect x="62" y="50" width="40" height="2"/><rect x="62" y="56" width="36" height="2"/><rect x="62" y="62" width="44" height="2"/></g>
      <rect x="62" y="68" width="74" height="12" fill="#f5f5f5" stroke="#ddd" stroke-width=".5"/>
      <rect x="110" y="83" width="13" height="4" fill="#5b8fd0"/><rect x="125" y="83" width="13" height="4" fill="#bdbdbd"/>
    </symbol>

    <symbol id="ui-dialog" viewBox="0 0 200 110" preserveAspectRatio="none">
      <rect width="200" height="110" fill="#fff"/>
      <rect width="200" height="6" fill="#2f7a3a"/>
      <rect x="0" y="6" width="200" height="8" fill="#eaeaea"/>
      <g stroke="#ececec" stroke-width=".6"><line x1="0" y1="24" x2="200" y2="24"/><line x1="0" y1="34" x2="200" y2="34"/><line x1="0" y1="44" x2="200" y2="44"/><line x1="0" y1="54" x2="200" y2="54"/><line x1="0" y1="64" x2="200" y2="64"/><line x1="0" y1="74" x2="200" y2="74"/><line x1="0" y1="84" x2="200" y2="84"/><line x1="0" y1="94" x2="200" y2="94"/></g>
      <rect x="8" y="10" width="120" height="80" fill="#f2f2f2" stroke="#8a8a8a" stroke-width=".8"/>
      <rect x="8" y="10" width="120" height="7" fill="#5b8fd0"/>
      <rect x="14" y="22" width="108" height="5" fill="#fff" stroke="#ccc" stroke-width=".5"/>
      <rect x="14" y="30" width="108" height="48" fill="#fff" stroke="#ccc" stroke-width=".5"/>
      <g fill="#c9c9c9"><rect x="18" y="34" width="40" height="2"/><rect x="18" y="40" width="52" height="2"/><rect x="18" y="46" width="36" height="2"/></g>
      <rect x="96" y="81" width="12" height="5" fill="#e6e6e6" stroke="#aaa" stroke-width=".4"/><rect x="110" y="81" width="12" height="5" fill="#e6e6e6" stroke="#aaa" stroke-width=".4"/>
      <g fill="#cfcfcf"><rect x="140" y="28" width="50" height="2"/><rect x="140" y="38" width="50" height="2"/><rect x="140" y="48" width="50" height="2"/><rect x="140" y="58" width="50" height="2"/><rect x="6" y="98" width="60" height="2"/></g>
    </symbol>

    <symbol id="ui-report" viewBox="0 0 120 80" preserveAspectRatio="none">
      <rect width="120" height="80" fill="#fff"/>
      <rect width="120" height="5" fill="#6e6e6e"/>
      <g fill="#dfe9f5"><rect x="4" y="8" width="112" height="4"/></g>
      <g stroke="#e5e5e5" stroke-width=".5"><line x1="4" y1="18" x2="116" y2="18"/><line x1="4" y1="24" x2="116" y2="24"/><line x1="4" y1="30" x2="116" y2="30"/><line x1="4" y1="36" x2="116" y2="36"/><line x1="4" y1="42" x2="116" y2="42"/><line x1="4" y1="48" x2="116" y2="48"/><line x1="4" y1="54" x2="116" y2="54"/><line x1="4" y1="60" x2="116" y2="60"/></g>
      <g fill="#bdbdbd"><rect x="6" y="14" width="24" height="2"/><rect x="6" y="20" width="20" height="2"/><rect x="6" y="26" width="26" height="2"/><rect x="6" y="32" width="18" height="2"/><rect x="6" y="38" width="24" height="2"/><rect x="6" y="44" width="22" height="2"/><rect x="6" y="50" width="26" height="2"/><rect x="6" y="56" width="20" height="2"/></g>
      <g fill="#8fbc3b"><rect x="40" y="13" width="6" height="4"/><rect x="40" y="25" width="6" height="4"/><rect x="52" y="19" width="6" height="4"/><rect x="52" y="37" width="6" height="4"/><rect x="40" y="49" width="6" height="4"/></g>
      <g fill="#d9534f"><rect x="40" y="19" width="6" height="4"/><rect x="52" y="31" width="6" height="4"/></g>
      <g fill="#e8b300"><rect x="52" y="13" width="6" height="4"/><rect x="40" y="37" width="6" height="4"/><rect x="52" y="49" width="6" height="4"/></g>
      <g fill="#cfcfcf"><rect x="66" y="14" width="46" height="2"/><rect x="66" y="20" width="40" height="2"/><rect x="66" y="26" width="46" height="2"/><rect x="66" y="32" width="36" height="2"/><rect x="66" y="38" width="46" height="2"/><rect x="66" y="44" width="42" height="2"/><rect x="66" y="50" width="46" height="2"/><rect x="66" y="56" width="38" height="2"/></g>
      <rect x="4" y="66" width="112" height="10" fill="#f5f5f5"/>
    </symbol>

    <symbol id="ui-dash" viewBox="0 0 220 80" preserveAspectRatio="none">
      <rect width="220" height="80" fill="#fff"/>
      <rect width="220" height="5" fill="#3a6fb0"/>
      <rect x="60" y="8" width="150" height="5" fill="#e6e6e6"/>
      <g fill="#5b8fd0"><rect x="6" y="10" width="30" height="2"/><rect x="10" y="16" width="26" height="2"/><rect x="10" y="22" width="30" height="2"/><rect x="14" y="28" width="22" height="2"/><rect x="14" y="34" width="26" height="2"/><rect x="10" y="40" width="28" height="2"/></g>
      <g fill="#d9534f"><rect x="10" y="50" width="40" height="2"/><rect x="10" y="56" width="34" height="2"/><rect x="10" y="62" width="44" height="2"/></g>
      <rect x="62" y="18" width="40" height="6" fill="#5b8fd0"/><rect x="62" y="27" width="28" height="6" fill="#8fbc3b"/><rect x="62" y="36" width="52" height="6" fill="#e8b300"/>
      <g fill="#bdbdbd"><rect x="130" y="18" width="40" height="2"/><rect x="130" y="24" width="34" height="2"/><rect x="130" y="30" width="44" height="2"/><rect x="130" y="36" width="30" height="2"/><rect x="180" y="18" width="28" height="2"/><rect x="180" y="24" width="24" height="2"/><rect x="180" y="30" width="28" height="2"/></g>
      <g stroke="#ececec" stroke-width=".5"><line x1="62" y1="50" x2="212" y2="50"/><line x1="62" y1="58" x2="212" y2="58"/><line x1="62" y1="66" x2="212" y2="66"/></g>
      <g fill="#cfcfcf"><rect x="64" y="53" width="50" height="2"/><rect x="64" y="61" width="42" height="2"/><rect x="64" y="69" width="48" height="2"/></g>
    </symbol>
  </defs>
</svg>

<!-- Cover -->
<section class="sheet cover" style="left:140px;top:60px">
  <div class="brand" style="left:90px;top:58px">
    <span class="name">Halde &amp; Wiegand</span>
    <span class="sub">project consulting</span>
    <span class="rule"></span>
  </div>
  <div class="photo" role="img" aria-label="Erde aus dem Weltall mit Wolkenwirbeln und Raumstation am Bildrand" style="left:95px;top:100px;width:175px;height:240px;background:radial-gradient(ellipse 60% 30% at 100% 20%,#1b1f26 0%,rgba(27,31,38,0) 100%),radial-gradient(ellipse 70% 50% at 40% 55%,#e4e8ec 0%,rgba(228,232,236,0) 70%),linear-gradient(165deg,#0e1218 0%,#3c4c62 18%,#9aa7b4 40%,#d3d9de 58%,#7f8c99 78%,#434f5d 100%)"></div>
  <div class="tagline" style="left:30px;top:245px">
    <span style="font-size:14px">Softwarelösungen</span>
    <span style="font-size:14px">für digitale</span>
    <span style="font-size:14px">Unternehmensprozesse</span>
  </div>
  <div class="page-foot" style="left:14px;right:14px"></div>
  <div class="page-foot-text" style="left:16px">HALDEWIEGAND.DE · QUILBYTE.DE</div>
</section>

<!-- Opening spread -->
<section class="sheet spread" style="left:620px;top:60px">
  <div class="photo" role="img" aria-label="Start einer Raumfähre am Startturm mit Rauchwolken vor blauem Himmel" style="left:0;top:0;width:270px;height:270px;background:radial-gradient(ellipse 60% 30% at 35% 85%,#f6f4ef 0%,rgba(246,244,239,0) 100%),radial-gradient(ellipse 25% 45% at 25% 45%,#b59b6a 0%,rgba(181,155,106,0) 100%),radial-gradient(ellipse 12% 35% at 58% 35%,#f2f2f0 0%,rgba(242,242,240,0) 100%),linear-gradient(180deg,#3f628f 0%,#7d9ac0 35%,#c9c3b4 65%,#ecebe6 100%)"></div>
  <div class="green-page" style="left:0;top:270px;width:270px;height:112px"></div>
  <div class="green-page" style="left:270px;width:270px"></div>
  <div class="brand light" style="left:420px;top:22px">
    <span class="name" style="font-size:10px">Halde &amp; Wiegand</span>
    <span class="sub" style="font-size:5.4px">project consulting</span>
    <span class="rule" style="height:1.5px"></span>
  </div>
  <div class="headline-bars" style="left:40px;top:140px">
    <span>Kommen Sie mit auf unsere</span>
    <span>digitale Arche Noah in die</span>
    <span>Zukunft des Projektmanagements!</span>
  </div>
  <div class="page-foot" style="left:300px;width:110px;bottom:30px;background:#fff"></div>
  <div class="page-foot" style="left:60px;width:110px;bottom:30px;background:#fff"></div>
</section>

<!-- Bold Bear -->
<section class="sheet spread" style="left:40px;top:560px">
  <div class="running-head" style="left:22px">Bold Bear</div>
  <div class="body-copy" style="left:22px;top:36px;width:120px">
    <p>Bold Bear ist die Lösung für ein erfolgreiches Projekt-, Programm- und Portfoliomanagement auf Basis von Veltrano Plan. Das zukunftsorientierte Tool hilft großen Unternehmen bei Planung und Steuerung ihrer Projekte und ermöglicht eine Kollaboration zwischen Projekten und Bereichen.</p>
  </div>
  <svg class="el" style="left:22px;top:98px" width="120" height="78" viewBox="0 0 120 78" role="img" aria-label="Architekturdiagramm der Systemebenen">
    <rect x="0.5" y="0.5" width="119" height="77" fill="#fff" stroke="#8fbc3b"/>
    <g fill="#8fbc3b"><rect x="8" y="8" width="22" height="5"/><rect x="8" y="26" width="16" height="5"/><rect x="8" y="42" width="18" height="5"/><rect x="8" y="58" width="20" height="5"/></g>
    <g fill="#9a9a9a"><rect x="40" y="10" width="10" height="5"/><rect x="40" y="30" width="10" height="5"/><rect x="40" y="50" width="10" height="5"/><rect x="40" y="66" width="14" height="4"/></g>
    <g stroke="#bbb" stroke-width=".6"><line x1="54" y1="12" x2="76" y2="11"/><line x1="54" y1="32" x2="76" y2="35"/><line x1="54" y1="52" x2="76" y2="59"/></g>
    <g fill="#d8d8d8"><rect x="78" y="8" width="34" height="6"/><rect x="78" y="20" width="34" height="6"/><rect x="78" y="32" width="34" height="6"/><rect x="78" y="44" width="34" height="6"/><rect x="78" y="56" width="34" height="6"/></g>
  </svg>
  <svg class="el" style="left:22px;top:185px" width="120" height="82" viewBox="0 0 120 82" role="img" aria-label="Stufenmodell der Projektmanagement-Reife mit Zahnradgrafik">
    <rect x="0.5" y="0.5" width="119" height="81" fill="#fff" stroke="#8fbc3b"/>
    <polygon points="8,76 22,8 36,76" fill="#d9eac0"/>
    <g stroke="#fff" stroke-width="1"><line x1="10" y1="60" x2="34" y2="60"/><line x1="14" y1="42" x2="30" y2="42"/><line x1="18" y1="24" x2="26" y2="24"/></g>
    <g fill="#9a9a9a"><rect x="38" y="18" width="12" height="2"/><rect x="38" y="40" width="12" height="2"/><rect x="38" y="62" width="12" height="2"/></g>
    <rect x="54" y="36" width="18" height="10" fill="none" stroke="#bbb" stroke-width=".5"/>
    <g fill="none" stroke="#8fbc3b" stroke-width="3"><circle cx="82" cy="44" r="6"/><circle cx="96" cy="38" r="5"/><circle cx="106" cy="48" r="5"/></g>
    <g fill="#9a9a9a"><rect x="80" y="14" width="26" height="2"/><rect x="80" y="18" width="20" height="2"/><rect x="82" y="62" width="22" height="2"/><rect x="82" y="66" width="18" height="2"/></g>
  </svg>
  <div class="caption" style="left:150px;top:230px;width:70px">Was ist hier zu sehen? Kurze Erläuterung zum Bild mit den wichtigsten Fakten für den Leser.</div>
  <div class="photo" role="img" aria-label="Braunbär im Porträt" style="left:270px;top:0;width:270px;height:275px;background:radial-gradient(ellipse 45% 55% at 58% 45%,#a27a4e 0%,#7b5a38 45%,rgba(90,66,44,0) 100%),radial-gradient(ellipse 30% 30% at 48% 60%,#c8a67e 0%,rgba(200,166,126,0) 100%),linear-gradient(100deg,#2f2a24 0%,#4d3a29 40%,#6a4d33 70%,#3b2d22 100%)"></div>
  <div class="product-title" style="left:300px;top:155px">Bold Bear</div>
  <div class="tagline" style="left:300px;top:178px">
    <span>Einfaches planen und steuern</span>
    <span>großer Projektportfolios und</span>
    <span>komplexer Programme</span>
  </div>
  <svg class="el" style="left:300px;top:245px" width="170" height="86" viewBox="0 0 170 86" role="img" aria-label="Diagramm zum Reifegrad im Projektmanagement">
    <rect x="0.5" y="0.5" width="169" height="85" fill="#fff" stroke="#8fbc3b"/>
    <line x1="12" y1="10" x2="12" y2="66" stroke="#999" stroke-width=".6"/>
    <line x1="12" y1="66" x2="160" y2="66" stroke="#999" stroke-width=".6"/>
    <polygon points="12,66 150,22 150,66" fill="#8fbc3b"/>
    <text x="96" y="12" font-size="3.6" fill="#666" font-family="Open Sans,sans-serif">Reifegrad im Projektmanagement</text>
    <text x="112" y="58" font-size="4.6" fill="#fff" font-family="Montserrat,sans-serif">Halde &amp; Wiegand</text>
    <text x="14" y="76" font-size="3.4" fill="#666" font-family="Open Sans,sans-serif">Basis</text>
    <text x="58" y="76" font-size="3.4" fill="#666" font-family="Open Sans,sans-serif">Standardisierung</text>
    <text x="112" y="76" font-size="3.4" fill="#666" font-family="Open Sans,sans-serif">Portfoliosteuerung</text>
  </svg>
  <div class="page-foot" style="left:22px;width:40px"></div>
  <div class="page-foot-text" style="left:290px">HALDE &amp; WIEGAND · 04</div>
</section>

<!-- Clever Cobra -->
<section class="sheet spread" style="left:620px;top:560px">
  <div class="photo" role="img" aria-label="Getarnte Schlange auf Laub und Ästen" style="left:0;top:0;width:300px;height:275px;background:radial-gradient(ellipse 40% 25% at 40% 70%,#d8cfbd 0%,rgba(216,207,189,0) 100%),radial-gradient(ellipse 35% 30% at 70% 35%,#5d564b 0%,rgba(93,86,75,0) 100%),radial-gradient(ellipse 40% 30% at 25% 30%,#b7ad9a 0%,rgba(183,173,154,0) 100%),linear-gradient(135deg,#7e766a 0%,#a59b88 40%,#6a6357 70%,#948a78 100%)"></div>
  <div class="product-title" style="left:20px;top:28px">Clever Cobra</div>
  <div class="tagline" style="left:20px;top:52px">
    <span>Risiko- und Issueportfolio</span>
    <span>übersichtlich dargestellt.</span>
  </div>
  <div class="running-head" style="right:22px">Clever Cobra</div>
  <svg class="screenshot" style="left:295px;top:118px;width:190px;height:115px" role="img" aria-label="Bildschirmansicht Risikomatrix und Tabelle"><use href="#ui-heat"/></svg>
  <div class="caption" style="left:340px;top:240px;width:145px">Was ist hier zu sehen? Kurze Erläuterung zum Bild mit den wichtigsten Fakten, damit der Leser die Funktion der Ansicht sofort erkennt.</div>
  <div class="body-copy" style="left:22px;top:295px;width:180px">
    <p>Clever Cobra dient zur grafischen und tabellarischen Aufbereitung des Risiko- und Issueportfolios. Damit werden kritische Zustände in Ihren Projekten noch schneller erkannt. Risiken und Issues können so gezielt adressiert werden.</p>
  </div>
  <div class="page-foot" style="left:22px;width:40px"></div>
  <div class="page-foot-text" style="left:290px">HALDE &amp; WIEGAND · 06</div>
</section>

<!-- Grand Lion -->
<section class="sheet spread" style="left:40px;top:1020px">
  <div class="photo" role="img" aria-label="Löwe mit Mähne im Profil" style="left:0;top:0;width:300px;height:272px;background:radial-gradient(ellipse 45% 55% at 45% 45%,#d9a25a 0%,#b87a34 45%,rgba(140,90,40,0) 100%),radial-gradient(ellipse 25% 30% at 70% 55%,#caa57a 0%,rgba(202,165,122,0) 100%),linear-gradient(100deg,#9b6128 0%,#b67a3a 40%,#7a5530 70%,#2f2d26 100%)"></div>
  <div class="product-title" style="left:35px;top:180px">Grand Lion</div>
  <div class="tagline" style="left:35px;top:203px">
    <span>Einfache und transparente</span>
    <span>Projektabbildung und –</span>
    <span>abwicklung in Veltrano Share</span>
  </div>
  <div class="running-head" style="right:22px">Grand Lion</div>
  <svg class="screenshot" style="left:338px;top:40px;width:130px;height:62px" role="img" aria-label="Bildschirmansicht Projektliste"><use href="#ui-list"/></svg>
  <svg class="screenshot" style="left:338px;top:115px;width:130px;height:65px" role="img" aria-label="Bildschirmansicht Projektdetails"><use href="#ui-list"/></svg>
  <div class="caption" style="left:338px;top:188px;width:72px">Was ist hier zu sehen? Kurze Erläuterung zum Bild mit den wichtigsten Fakten für den Leser.</div>
  <svg class="screenshot" style="left:338px;top:280px;width:130px;height:55px" role="img" aria-label="Bildschirmansicht Aufgabenübersicht"><use href="#ui-list"/></svg>
  <div class="body-copy" style="left:35px;top:288px;width:85px">
    <p>Grand Lion erweitert den bestehenden Standardumfang von Veltrano Share um Fähigkeiten für ein echtes Multiprojektmanagement.</p>
  </div>
  <div class="body-copy" style="left:128px;top:288px;width:90px">
    <p>Im Fokus stehen die Bedarfsfelder Controlling und Kostenreflexion. Grand Lion ist die optimale Lösung für die professionelle Projektverwaltung im Mittelstand.</p>
  </div>
  <div class="page-foot" style="left:290px;width:40px"></div>
  <div class="page-foot-text" style="left:230px">HALDE &amp; WIEGAND · 08</div>
</section>

<!-- Swift Leopard -->
<section class="sheet spread" style="left:620px;top:1020px">
  <div class="running-head" style="left:22px">Swift Leopard</div>
  <div class="body-copy" style="left:22px;top:36px;width:125px">
    <p>Swift Leopard vereinfacht das Statusberichtswesen für die Kommunikation zwischen Projekt und Management und erstellt übersichtliche Berichte.</p>
    <p>Die visuell ansprechenden Berichte werden automatisch generiert und sind einfach konfigurierbar. So kann jederzeit auf die individuellen Bedürfnisse Ihres Unternehmens eingegangen werden. Die Reports sorgen für klare Verhältnisse.</p>
  </div>
  <div class="caption" style="left:22px;top:180px;width:60px">Was ist hier zu sehen? Kurze Erläuterung zum Bild mit den wichtigsten Fakten für den Leser.</div>
  <svg class="screenshot" style="left:22px;top:238px;width:118px;height:80px" role="img" aria-label="Bildschirmansicht Statusbericht"><use href="#ui-report"/></svg>
  <div class="photo" role="img" aria-label="Leopard im Porträt vor grünem Laub" style="left:250px;top:0;width:290px;height:272px;background:radial-gradient(ellipse 40% 50% at 40% 50%,#d8b878 0%,#b08a50 45%,rgba(140,110,60,0) 100%),radial-gradient(ellipse 30% 30% at 35% 80%,#e8e2d2 0%,rgba(232,226,210,0) 100%),linear-gradient(90deg,#4e5f36 0%,#6f6a40 40%,#4d6a35 70%,#2e4325 100%)"></div>
  <div class="product-title" style="left:315px;top:62px">Swift Leopard</div>
  <div class="tagline" style="left:315px;top:86px">
    <span>Ihre Projektkommunikation</span>
    <span>einfach standardisiert</span>
  </div>
  <svg class="el" style="left:300px;top:250px" width="200" height="84" viewBox="0 0 200 84" role="img" aria-label="Statusübersicht mit Ampeln">
    <rect x="0.5" y="0.5" width="199" height="83" fill="#fff" stroke="#8fbc3b"/>
    <text x="8" y="10" font-size="4" fill="#555" font-family="Open Sans,sans-serif">Projektstatus · Übersicht</text>
    <g stroke="#e2e2e2" stroke-width=".5"><line x1="6" y1="18" x2="194" y2="18"/><line x1="6" y1="30" x2="194" y2="30"/><line x1="6" y1="42" x2="194" y2="42"/><line x1="6" y1="54" x2="194" y2="54"/><line x1="6" y1="66" x2="194" y2="66"/></g>
    <g fill="#bbb"><rect x="8" y="22" width="26" height="3"/><rect x="8" y="34" width="22" height="3"/><rect x="8" y="46" width="28" height="3"/><rect x="8" y="58" width="20" height="3"/><rect x="8" y="70" width="24" height="3"/></g>
    <g><circle cx="70" cy="24" r="2" fill="#d33"/><circle cx="82" cy="24" r="2" fill="#6a3"/><circle cx="94" cy="24" r="2" fill="#6a3"/>
    <circle cx="70" cy="36" r="2" fill="#e8b300"/><circle cx="82" cy="36" r="2" fill="#6a3"/><circle cx="94" cy="36" r="2" fill="#d33"/>
    <circle cx="70" cy="48" r="2" fill="#6a3"/><circle cx="82" cy="48" r="2" fill="#e8b300"/><circle cx="94" cy="48" r="2" fill="#6a3"/>
    <circle cx="70" cy="60" r="2" fill="#d33"/><circle cx="82" cy="60" r="2" fill="#6a3"/><circle cx="94" cy="60" r="2" fill="#e8b300"/>
    <circle cx="70" cy="72" r="2" fill="#6a3"/><circle cx="82" cy="72" r="2" fill="#6a3"/><circle cx="94" cy="72" r="2" fill="#6a3"/></g>
    <g fill="#ccc"><rect x="110" y="22" width="20" height="3"/><rect x="110" y="34" width="20" height="3"/><rect x="110" y="46" width="20" height="3"/><rect x="110" y="58" width="20" height="3"/><rect x="110" y="70" width="20" height="3"/></g>
    <g fill="#5b8fd0"><rect x="150" y="22" width="34" height="3"/><rect x="150" y="34" width="34" height="3"/><rect x="150" y="46" width="34" height="3"/><rect x="150" y="58" width="34" height="3"/></g>
  </svg>
  <div class="page-foot" style="left:22px;width:40px"></div>
  <div class="page-foot-text" style="left:290px">HALDE &amp; WIEGAND · 10</div>
</section>

<!-- Quiet Buffalo -->
<section class="sheet spread" style="left:40px;top:1480px">
  <div class="running-head" style="left:22px">Quiet Buffalo</div>
  <div class="caption" style="left:22px;top:34px;width:60px">Was ist hier zu sehen? Kurze Erläuterung zum Bild mit den wichtigsten Fakten für den Leser.</div>
  <svg class="screenshot" style="left:22px;top:88px;width:180px;height:105px" role="img" aria-label="Bildschirmansicht Ressourcenanfrage"><use href="#ui-gantt"/></svg>
  <svg class="screenshot" style="left:22px;top:208px;width:180px;height:110px" role="img" aria-label="Bildschirmansicht Genehmigungsdialog"><use href="#ui-dialog"/></svg>
  <div class="photo" role="img" aria-label="Hochlandrind mit langen Hörnern in Graslandschaft unter Wolkenhimmel" style="left:210px;top:0;width:330px;height:270px;background:radial-gradient(ellipse 25% 35% at 50% 55%,#7a4e30 0%,#5d3b25 50%,rgba(93,59,37,0) 100%),radial-gradient(ellipse 50% 25% at 55% 20%,#c3ccd3 0%,rgba(195,204,211,0) 100%),linear-gradient(180deg,#4e6480 0%,#94a4b2 30%,#b1b2a8 52%,#8a7d55 72%,#6c6a44 100%)"></div>
  <div class="product-title" style="left:295px;top:160px">Quiet Buffalo</div>
  <div class="tagline" style="left:295px;top:183px">
    <span>Digitalisierung Ihres</span>
    <span>Ressourcengenehmigungsprozess</span>
    <span>in Veltrano Plan</span>
  </div>
  <div class="body-copy" style="left:295px;top:285px;width:180px">
    <p>Quiet Buffalo unterstützt die Kommunikation zwischen Ressourcenmanagern und Projektleitern. Der Bedarf und die Freigabe von Ressourcen wird durch Quiet Buffalo zentral und unabhängig verwaltet und mögliche Abweichungen transparent abgebildet.</p>
  </div>
  <div class="page-foot" style="left:22px;width:40px"></div>
  <div class="page-foot-text" style="left:290px">HALDE &amp; WIEGAND · 12</div>
</section>

<!-- Gentle Elephant -->
<section class="sheet spread" style="left:620px;top:1480px">
  <div class="photo" role="img" aria-label="Afrikanischer Elefant in Buschlandschaft" style="left:0;top:0;width:300px;height:272px;background:radial-gradient(ellipse 30% 40% at 35% 40%,#5f5e5a 0%,#4a4a47 50%,rgba(74,74,71,0) 100%),radial-gradient(ellipse 40% 20% at 50% 90%,#a8925e 0%,rgba(168,146,94,0) 100%),linear-gradient(160deg,#5f6f48 0%,#838463 35%,#6c6b5c 60%,#9a8b60 100%)"></div>
  <div class="product-title" style="left:25px;top:168px">Gentle Elephant</div>
  <div class="tagline" style="left:25px;top:192px">
    <span>Einfache Abbildung Ihrer</span>
    <span>Projektstruktur in</span>
    <span>individuellen Dashboards.</span>
  </div>
  <div class="running-head" style="right:22px">Gentle Elephant</div>
  <div class="body-copy" style="left:335px;top:38px;width:130px">
    <p>Benutzer können sich ihr individuelles Dashboard zusammenstellen und erhalten mit nur einem Klick alle für sie relevanten Projektinformationen.</p>
    <p>Bilden Sie Ihre Projektstruktur ab und erhalten Sie damit bequem Informationen zu ausgewählten Projekten. Welche Vorgänge verspätet sind und welche Meilensteine anstehen, behalten Sie genauso im Blick.</p>
  </div>
  <svg class="screenshot" style="left:270px;top:245px;width:220px;height:80px" role="img" aria-label="Bildschirmansicht Dashboard"><use href="#ui-dash"/></svg>
  <div class="page-foot" style="left:22px;width:40px"></div>
  <div class="page-foot-text" style="left:290px">HALDE &amp; WIEGAND · 14</div>
</section>

<!-- Partner -->
<section class="sheet spread" style="left:40px;top:1940px">
  <div class="green-page" style="left:0;width:305px"></div>
  <div class="running-head" style="left:22px;color:#fff">Veltrano Gold Partner</div>
  <div class="partner-box" style="left:22px;top:36px;width:165px;height:285px">
    <div class="body-copy" style="position:static;width:140px">
      <p>Unser junges und dynamisches Team ist als Veltrano Gold Partner seit 10 Jahren auf Projekt- und Prozessmanagement mit Veltrano Technologien spezialisiert.</p>
      <p>Unsere Spezialisierung auf Portfolio-, Programm- und Projektmanagement mit Veltrano Plan und Veltrano Share sowie die Abdeckung aller relevanten Fähigkeiten sichern Ihnen eine kompetente Begleitung Ihrer Projekte.</p>
    </div>
    <div class="partner-row" style="margin-top:30px;gap:8px">
      <span class="partner-name" style="color:#d0551b"><i style="background:#d0551b"></i>Veltrano 365</span>
      <span class="partner-name" style="color:#2f7a3a"><i style="background:#2f7a3a"></i>Veltrano Plan</span>
      <span class="partner-name" style="color:#1f6fb5"><i style="background:#1f6fb5"></i>Veltrano Share</span>
    </div>
    <div class="partner-row">
      <span class="partner-word">H&amp;W</span>
      <span class="partner-word">quilbyte</span>
    </div>
    <div class="badge">
      <div class="badge-shape"></div>
      <div class="badge-lines">Gold Projekt- und Portfoliomanagement<br>Gold Application Development<br>Silver Cloud Platform</div>
    </div>
  </div>
  <div class="photo" role="img" aria-label="Erde aus dem Weltall" style="left:305px;top:0;width:235px;height:26px;background:linear-gradient(90deg,#0d1a2e,#2e4a70 60%,#6f8fb4)"></div>
  <div class="photo" role="img" aria-label="Tablet mit Dashboard-Auswertung" style="left:312px;top:40px;width:88px;height:62px;background:radial-gradient(ellipse 38% 34% at 50% 48%,#f2f4f6 0%,#dfe4ea 60%,rgba(223,228,234,0) 100%),linear-gradient(135deg,#222 0%,#444 50%,#2a2a2a 100%)"></div>
  <div class="body-copy" style="left:410px;top:34px;width:115px">
    <p>Auswertbarkeit ist das A und O einer erfolgreichen Unternehmens- und Projektsteuerung. Reports, Dashboards und Technologien zur Business Intelligence helfen Ihnen, die drängendsten Themen noch besser zu identifizieren.</p>
  </div>
  <div class="body-copy" style="left:312px;top:122px;width:210px">
    <p>Ob individuell entwickelt oder Ready-to-Use mit Veltrano Insight, Halde &amp; Wiegand ist Ihr Partner, um stets den Überblick zu behalten.</p>
  </div>
  <div class="photo" role="img" aria-label="Mehrere Bildschirme und Geräte mit Diagrammen" style="left:312px;top:180px;width:88px;height:60px;background:radial-gradient(ellipse 30% 35% at 35% 45%,#2b2b2b 0%,#555 60%,rgba(85,85,85,0) 100%),radial-gradient(ellipse 20% 30% at 75% 60%,#3a3a3a 0%,rgba(58,58,58,0) 100%),linear-gradient(135deg,#f2f2f2,#d4d4d4)"></div>
  <div class="section-heading" style="left:312px;top:255px">Veltrano Insight</div>
  <div class="body-copy" style="left:312px;top:268px;width:205px">
    <p>Veltrano Insight ist eine Suite aus Analysetools, die Einblicke in alle Bereiche Ihrer Organisation liefern. Stellen Sie Verbindungen mit Hunderten von Datenquellen her, vereinfachen Sie die Datenaufbereitung und erstellen Sie ansprechende Berichte für das Web oder mobile Geräte.</p>
  </div>
  <div class="page-foot" style="left:22px;width:40px;background:#fff"></div>
  <div class="page-foot-text" style="left:320px">HALDE &amp; WIEGAND · 16</div>
</section>

<!-- About -->
<section class="sheet spread" style="left:620px;top:1940px">
  <div class="running-head" style="left:22px">Warum Halde &amp; Wiegand</div>
  <div class="body-copy" style="left:22px;top:36px;width:175px">
    <p>Langjährige Erfahrung und tiefgreifende Expertise<br>Konzentriertes Expertenwissen im Bereich Veltrano Technologien<br>Durchführung einer Vielzahl von Kundenprojekten<br>Enger Kontakt und Austausch mit Veltrano<br>Schnelle Reaktionszeit und zuverlässige Aufgabenlösung<br>Exzellent ausgebildete und zertifizierte Mitarbeiter<br>Prozessverständnis vor der IT-Umsetzung<br>Engagement in wissenschaftlichen und fachlichen Institutionen<br>Motiviertes, internationales und dynamisches Team<br>Ausbildungsbetrieb – wir investieren in den Nachwuchs</p>
  </div>
  <div class="quote-box" style="left:22px;top:150px;width:165px;height:82px">
    <div class="quote">Musterfirma ipsam ex est et aut o minisque molo est, id mincimpost rem tem andes ius, officte vendunti no</div>
    <div class="author">Max Mustermann,<br>Musterfirma</div>
  </div>
  <div class="quote-box" style="left:22px;top:248px;width:165px;height:82px">
    <div class="quote">Musterfirma ipsam ex est et aut o minisque molo est, id mincimpost rem tem andes ius, officte vendunti no</div>
    <div class="author">Max Mustermann,<br>Musterfirma</div>
  </div>
  <div class="photo" role="img" aria-label="Raumstation mit Roboterarm und Solarmodulen über der Erde" style="left:262px;top:0;width:278px;height:382px;background:radial-gradient(ellipse 18% 40% at 52% 35%,#c9ccd0 0%,rgba(201,204,208,0) 100%),radial-gradient(ellipse 28% 14% at 45% 80%,#e3e3e0 0%,rgba(227,227,224,0) 100%),radial-gradient(ellipse 35% 6% at 60% 72%,#3b4660 0%,rgba(59,70,96,0) 100%),linear-gradient(170deg,#050608 0%,#111419 45%,#35557c 72%,#9bb6d0 100%)"></div>
  <div class="page-foot" style="left:22px;width:40px"></div>
</section>

</body>
</html>
```